WALKING FOOD TOURISM BUSINESS. REQUEST FOR DIGITAL BROCHURE

Our business is a walking food tourism business in and around Melbourne's central city. We are needing a e-digital brochure - to be solely used as email' marketing content, not print. Therefore PDF size needs to be appropriate/suitable. Please see attached written content required for the brochure - together with our logo. For images, I am happy for designer to use our website content (www.wanderplatekitchen.com). OR any other appropriate and creative 'foodie' or Melbourne image suitable. Many thanks:)

Target Market(s)

Premium brand travellers or local adventurous Australians.

Requirements
Must have
• Quality font and images
Nice to have
• Quality Melbourne and food images. See website - wanderplatekitchen.com
Should not have
• Too much colour. Brand is black and white, sophisticated, premium product.

```html
<!DOCTYPE html>
<html lang="en">
<head>
<meta charset="utf-8">
<title>Wander Plate — Digital Brochure</title>
<link href="https://fonts.googleapis.com/css2?family=Montserrat:wght@400;500;600;700&display=swap" rel="stylesheet">
<style>
:root{
  --stage:#efefef;
  --navy:#1b2233;
  --navy-deep:#141a28;
  --blue:#1a63d4;
  --blue-light:#3d8ae8;
  --gold:#f0a83a;
  --white:#ffffff;
  --ink:#1d1d1f;
  --sky-pale:#a9c9f2;
}
*{box-sizing:border-box;margin:0;padding:0}
html,body{width:1200px;height:996px;overflow:hidden;background:var(--stage);font-family:'Montserrat',sans-serif}
.spread{position:relative;width:1200px;height:996px}
.page{position:absolute;width:540px;height:408px;overflow:hidden;box-shadow:0 4px 14px rgba(0,0,0,.28)}
.page--cover{left:42px;top:59px;background:var(--blue)}
.page--tours{left:618px;top:59px;background:var(--navy)}
.page--evening{left:42px;top:498px;background:var(--navy)}
.page--contact{left:618px;top:498px;background:var(--white)}
.photo{position:absolute}
.brand-name{font-family:'Montserrat',sans-serif;font-weight:600;letter-spacing:.5px;line-height:1;display:flex;align-items:center;gap:8px}
.brand-name .dot{width:10px;height:10px;border-radius:50%;background:currentColor;display:inline-block}

/* cover */
.cover__skyline{left:0;top:120px;width:540px;height:288px;
  background:linear-gradient(180deg,rgba(26,99,212,0) 0%,#6fa7e6 12%,#9ac0ea 35%,#6f8fb0 58%,#7a8c8f 70%,#4d6a78 82%,#37505c 100%)}
.cover__brand{position:absolute;left:32px;top:52px;color:var(--white);font-size:22px}
.cover__intro{position:absolute;left:274px;top:38px;width:258px;text-align:center;color:var(--white)}
.cover__title{font-size:10px;font-weight:700;letter-spacing:.3px;margin-bottom:8px}
.cover__text{font-size:8px;line-height:1.5}
.polaroid{position:absolute;background:var(--white);padding:5px 5px 12px;box-shadow:0 2px 6px rgba(0,0,0,.35)}
.polaroid .photo{position:static;width:100%;height:100%}
.polaroid--a{left:18px;top:117px;width:111px;height:96px;transform:rotate(-2deg)}
.polaroid--b{left:30px;top:206px;width:111px;height:96px;transform:rotate(2deg)}
.polaroid--c{left:21px;top:305px;width:117px;height:82px;transform:rotate(-3deg)}
.polaroid .photo{background:linear-gradient(160deg,#6d6a66,#3e3b3a 60%,#8c7c6a)}

/* tours */
.tours__label{position:absolute;left:0;top:0;width:21px;height:135px;display:flex;align-items:center;justify-content:center}
.tours__label span{writing-mode:vertical-rl;transform:rotate(180deg);color:var(--white);font-weight:700;font-size:10px;letter-spacing:1px}
.tour{position:absolute;color:var(--white);text-align:center;padding:0 12px;display:flex;flex-direction:column;justify-content:center}
.tour__name{font-size:9.5px;font-weight:700;margin-bottom:3px}
.tour__meta{font-size:5px;color:var(--gold);margin-bottom:6px}
.tour__text{font-size:6.1px;line-height:1.5}
.tour--bucket{left:21px;top:0;width:238px;height:135px;background:linear-gradient(180deg,var(--navy-deep),var(--navy))}
.tour--street{left:275px;top:135px;width:265px;height:137px}
.tour--story{left:0;top:272px;width:262px;height:136px}
.tours__photo-top{left:259px;top:0;width:281px;height:135px;background:linear-gradient(135deg,#c9826f,#e6b7a4 45%,#7a5637)}
.tours__photo-mid{left:14px;top:135px;width:261px;height:137px;background:linear-gradient(120deg,#ece4d4,#8e5a3a 45%,#e9e1d0 75%,#6a7b3a)}
.tours__photo-low{left:262px;top:272px;width:278px;height:136px;background:linear-gradient(180deg,#9fc2e6 0%,#b7c6d4 35%,#6d6c66 60%,#4b5d66 100%)}

/* evening */
.evening__photo-top{left:0;top:0;width:279px;height:176px;background:linear-gradient(135deg,#5a3a2a,#d8b27a 40%,#f0a24e 60%,#cfcfcf 80%)}
.evening__photo-mid{left:279px;top:176px;width:261px;height:160px;background:linear-gradient(160deg,#d9dee3,#8a7a6e 50%,#3b3d44)}
.evening__panel{position:absolute;left:279px;top:0;width:261px;height:176px;background:linear-gradient(180deg,var(--navy-deep),var(--navy) 70%,#4a5870);padding:0 16px;display:flex;flex-direction:column;justify-content:center;text-align:center;color:var(--white)}
.evening__private{position:absolute;left:0;top:176px;width:279px;height:160px;padding:0 16px;display:flex;flex-direction:column;justify-content:center;text-align:center;color:var(--white)}
.evening__band{position:absolute;left:0;top:336px;width:540px;height:72px;background:linear-gradient(180deg,#3a4256,#1b2233);color:var(--white);text-align:center;font-size:7px;line-height:1.6;padding:12px 80px 0}
.evening__band strong{font-weight:700}

/* contact */
.contact__sky{position:absolute;left:0;top:0;width:319px;height:140px;background:linear-gradient(180deg,#8fb6ee,rgba(255,255,255,0))}
.contact__photo{left:319px;top:0;width:221px;height:408px;background:linear-gradient(180deg,#7a5a3a,#c89a5c 35%,#a68660 60%,#6e6a66 85%,#5a4a3e)}
.contact__info{position:absolute;left:33px;top:74px;color:var(--ink)}
.contact__heading{font-size:8.5px;font-weight:700;margin-bottom:5px}
.contact__line{display:flex;align-items:center;gap:6px;font-size:8.5px;margin:0 0 3px 10px}
.contact__line .dot{width:8px;height:8px;border-radius:50%;background:var(--ink)}
.contact__gap{height:8px}
.contact__policy{position:absolute;left:33px;top:187px;width:250px;color:var(--ink)}
.contact__policy h3{font-size:7.5px;font-weight:700;margin-bottom:3px}
.contact__policy li{font-size:7.5px;line-height:1.5;margin-left:10px}
.contact__brand{position:absolute;left:40px;top:340px;color:var(--ink);font-size:24px}
</style>
</head>
<body>
<main class="spread">

  <section class="page page--cover">
    <div class="photo cover__skyline" role="img" aria-label="Melbourne city skyline above the Yarra River and a stone bridge"></div>
    <div class="cover__brand brand-name"><span class="dot"></span>wander plate</div>
    <div class="cover__intro">
      <h1 class="cover__title">WANDER PLATE EXPERIENCES</h1>
      <p class="cover__text">We provide experiential adventure for visitors and locals alike – all through the 'lens' of exceptional food. Our tour experiences capture the essence of Melbourne, its people and diverse history – stopping to sip, savour and delight in Melbourne's foodie hot spots &amp; indulging in their signature tastes.</p>
    </div>
    <div class="polaroid polaroid--a"><div class="photo" role="img" aria-label="Tour group gathered on a city street"></div></div>
    <div class="polaroid polaroid--b"><div class="photo" role="img" aria-label="Guests posing in a laneway"></div></div>
    <div class="polaroid polaroid--c"><div class="photo" role="img" aria-label="Guests tasting food at a market stall"></div></div>
  </section>

  <section class="page page--tours">
    <div class="tours__label"><span>OUR EXPERIENCES</span></div>
    <div class="photo tours__photo-top" role="img" aria-label="Close-up of a plated seafood dish with herbs"></div>
    <div class="photo tours__photo-mid" role="img" aria-label="Steamed bao buns filled with crispy chicken and slaw"></div>
    <div class="photo tours__photo-low" role="img" aria-label="Yarra River promenade with boats and city towers"></div>
    <div class="tour tour--bucket">
      <h2 class="tour__name">Foodies Bucket List Tour</h2>
      <p class="tour__meta">3.5 hours / A$118 Adult / A$59 Child / Up to 8 guests</p>
      <p class="tour__text">Think you're a foodie? Are you torn by delicious culinary choices and have a fear of missing out on the true Melbourne foodie experience? If your answers are 'yes', then our 'Bucket List' adventure is for you.<br>When time is of the essence, our 'Bucket List Tour' will 'wow' your senses – while tasting and strolling your way through Melbourne's exploding culinary epicentre.</p>
    </div>
    <div class="tour tour--street">
      <h2 class="tour__name">Street Eats Tour</h2>
      <p class="tour__meta">3 hours / A$118 Adult / A$59 Child / Up to 10 guests</p>
      <p class="tour__text">Hungry? Then why not broaden your palette and TAKE IT TO THE STREETS – Melbourne style. Our Street Eats Tour is ideal for locals and visitors, keen to wander, explore &amp; taste Melbourne's Asian 'street food' scene. Taste your way in and around Melbourne – slurping up Thai noodles, devouring Shanghai Dumplings, Korean bites, Japanese treats and more – whilst taking in mystical immigrant stories – from the Chinese arrival, the Vietnamese and later, the sub-continent. The perfect experience to capture some of Melbourne's best, hidden treasures.</p>
    </div>
    <div class="tour tour--story">
      <h2 class="tour__name">The Story of Melbourne</h2>
      <p class="tour__meta">2.5 hours / A$98 Adult / A$49 Child / Up to 12 guests</p>
      <p class="tour__text">From the Yarra River to Iconic Laneways, Historic Precincts, Theatres &amp; Cathedrals – discover the character, culture &amp; community of our magnificent city, that is MELBOURNE. Walk with us on tour, as we share stories about Melbourne's past and present. Along your journey you'll take in the very fabric of Melbourne. From the early beginnings – through to today, soaking in why Melbourne continues to be one of the greatest multi-cultural cities in the world.</p>
    </div>
  </section>

  <section class="page page--evening">
    <div class="photo evening__photo-top" role="img" aria-label="Baked pasta dish in a copper pan beside a glass of wine"></div>
    <div class="evening__panel">
      <h2 class="tour__name">Evening Palate &amp; Pairing</h2>
      <p class="tour__meta">3 hours / A$168 Adult / A$84 Child / Up to 8 guests</p>
      <p class="tour__text">Enjoy your evening in one of Melbourne most vibrant, mouth-watering, delectable foodie precincts. You'll be 'wowed' by Melbourne's charm and hospitality as you experience signature tastes from some of our best restaurants – pairing flavours and textures at each venue – and hearing the stories that transformed Melbourne into the marvellous 'food capital' city it is today.</p>
    </div>
    <div class="evening__private">
      <h2 class="tour__name">Private Experiences</h2>
      <p class="tour__meta">Up to 8 hours / Tailored itineraries</p>
      <p class="tour__text">Our private tours are ideal for the ultimate fun 'group adventure'. Share and experience the cultural delights of Melbourne with good friends – perhaps a team building event, a family reunion, a special birthday or wedding party. All with your very own personal tour host.</p>
    </div>
    <div class="photo evening__photo-mid" role="img" aria-label="Group of friends sharing a meal at a restaurant table"></div>
    <div class="evening__band">Choose from one of our <strong>Wander Plate Experiences</strong> – with the option to customise the tour length, start time and tour distance covered. OR tailor your own experience to suit your interest, theme, community and corporate groups. Either way, your PRIVATE EXPERIENCE will be created with you in mind.<br>Enquiries: <strong>info@wanderplatekitchen.com</strong></div>
  </section>

  <section class="page page--contact">
    <div class="contact__sky"></div>
    <div class="photo contact__photo" role="img" aria-label="Ornate Victorian shopping arcade with mosaic floor"></div>
    <div class="contact__info">
      <h2 class="contact__heading">For Booking Schedule &amp; Enquiry :</h2>
      <p class="contact__line">
        <svg width="9" height="9" viewBox="0 0 24 24" aria-hidden="true"><path fill="#1d1d1f" d="M6.6 10.8a15.1 15.1 0 0 0 6.6 6.6l2.2-2.2c.3-.3.7-.4 1-.2 1.1.4 2.3.6 3.6.6.6 0 1 .4 1 1V20c0 .6-.4 1-1 1A17 17 0 0 1 3 4c0-.6.4-1 1-1h3.5c.6 0 1 .4 1 1 0 1.3.2 2.5.6 3.6.1.3 0 .7-.2 1z"/></svg>
        +61 400 555 019</p>
      <div class="contact__gap"></div>
      <h2 class="contact__heading">Social Media :</h2>
      <p class="contact__line"><span class="dot"></span>wanderplate.kitchen</p>
      <p class="contact__line"><span class="dot"></span>WanderPlate.Kitchen</p>
    </div>
    <div class="contact__policy">
      <h3>Cancellation &amp; Amendments</h3>
      <ul>
        <li>100% REFUND for cancellations outside 24 hours of the tour departure time</li>
        <li>NO REFUND for cancellations made within 24 hours of the tour departure time</li>
      </ul>
    </div>
    <div class="contact__brand brand-name"><span class="dot"></span>wander plate</div>
  </section>

</main>
</body>
</html>
```